Professional business card for the wholesale of metals, chemicals and waste

We are an established company in the wholesale trade of metals, chemicals and waste and are looking for a creative, professional design for our business card. The business card should reflect the values of our company - competence, reliability and innovative strength. It should convey both industry expertise and a modern, trustworthy image.
Important information for the design:

Logo: Our company logo must be prominently placed on the business card.
Colors: Please refer to the colors used on our website www.okr-gmbh.at. These colors should appear in the design to maintain the visual identity of our company.

QR Code: The business card should contain a QR code that contains all the information listed on the business card.
Font: Choose clear, easy-to-read fonts that reflect a modern, professional look.
Layout: The design should be clear and structured so that both text and visual elements (logo, QR code) are in a balanced relationship to each other.

Information that should appear on the business card:

Company name: OKR Handelsagenturen GmbH
Title: Dipl.-Ing.
Name: Lukas Fenwald
Position: Managing Director of Operations & Corporate Development
Phone: +43 4186 5921 48
Mobile: +43 664 58 37 216
Email: lukas.fenwald@okr-gmbh.at
Homepage: www.okr-gmbh.at

Design style:

Industry: Industrial yet modern style that conveys competence and trust.
Message: The business card should present our company as a leading supplier in the wholesale trade of metals, chemicals and waste – reliable, professional and innovative.
Target group: Our target group consists of B2B customers and industry contacts who are looking for high-quality products and services in the areas of metal trading, chemicals and waste management.

We look forward to creative designs that reflect our professional identity and are also modern and appealing. Your design should make a statement for our company!

```html
<!DOCTYPE html>
<html lang="en">
<head>
<meta charset="utf-8">
<title>OKR Handelsagenturen GmbH – Business Card</title>
<link href="https://fonts.googleapis.com/css2?family=Roboto:ital,wght@0,300;0,400;0,500;0,700;1,400&display=swap" rel="stylesheet">
<style>
  :root {
    --navy: #1e2249;
    --white: #ffffff;
    --backdrop: #a7a7a9;
    --shadow: rgba(0, 0, 0, 0.28);
  }
  * { margin: 0; padding: 0; box-sizing: border-box; }
  html, body {
    width: 1200px; height: 1200px; overflow: hidden;
    background: var(--backdrop);
    font-family: "Roboto", Arial, sans-serif;
    color: var(--navy);
  }
  .card {
    position: absolute; left: 160px; width: 880px; height: 516px;
    box-shadow: 2px 4px 10px var(--shadow);
    overflow: hidden;
  }
  .card--front { top: 62px; background: var(--white); }
  .card--back { top: 625px; background: var(--navy); }

  /* front */
  .brand { position: absolute; left: 84px; top: 100px; width: 200px; text-align: center; }
  .brand__name { font-size: 78px; font-weight: 700; line-height: 1; letter-spacing: 2px; }
  .brand__title { margin-top: 60px; font-size: 28px; font-weight: 700; }

  .identity {
    position: absolute; left: 440px; top: 3px; width: 396px; height: 287px;
    background: var(--navy); color: var(--white); text-align: right;
    padding: 94px 22px 0 0;
  }
  .identity__name { font-size: 35px; font-weight: 500; line-height: 1; }
  .identity__role { margin-top: 16px; font-size: 20px; font-style: italic; font-weight: 400; line-height: 30px; }
  .rule { position: absolute; left: 440px; width: 396px; height: 5px; background: var(--navy); }
  .rule--one { top: 294px; }
  .rule--two { top: 307px; }

  .phones {
    position: absolute; left: 0; top: 372px; width: 374px; height: 114px;
    background: var(--navy); color: var(--white);
    padding: 26px 0 0 66px;
  }
  .contact { list-style: none; font-size: 24px; font-weight: 300; }
  .contact li { display: flex; align-items: center; height: 40px; }
  .contact svg { width: 16px; height: 16px; margin-right: 22px; flex: none; }
  .online { position: absolute; left: 418px; top: 398px; }
  .online.contact { font-weight: 400; }

  /* back */
  .glow { position: absolute; left: 0; top: 0; width: 880px; height: 516px; }
  .back-brand {
    position: absolute; left: 0; width: 880px; text-align: center;
    top: 178px; font-size: 112px; font-weight: 700; color: var(--white);
    letter-spacing: 4px; line-height: 1;
  }
  .back-title {
    position: absolute; left: 0; width: 880px; text-align: center;
    top: 372px; font-size: 43px; font-weight: 700; color: var(--navy);
  }
</style>
</head>
<body>

<section class="card card--front">
  <div class="brand">
    <div class="brand__name">OKR</div>
    <div class="brand__title">Dipl.-Ing.</div>
  </div>

  <div class="identity">
    <div class="identity__name">Lukas Fenwald</div>
    <div class="identity__role">Managing Director of Operations<br>&amp; Corporate Development</div>
  </div>
  <div class="rule rule--one"></div>
  <div class="rule rule--two"></div>

  <div class="phones">
    <ul class="contact">
      <li>
        <svg viewBox="0 0 16 16" aria-hidden="true"><path fill="currentColor" d="M3.2 1.5 5.6 1l1.3 3.3-1.6 1.2a8 8 0 0 0 5.2 5.2l1.2-1.6L15 10.4l-.5 2.4c-.2.9-1 1.4-1.9 1.3C6.9 13.5 2.5 9.1 1.9 3.4c-.1-.9.4-1.7 1.3-1.9z"/></svg>
        +43 4186 5921 48
      </li>
      <li>
        <svg viewBox="0 0 16 16" aria-hidden="true"><path fill="currentColor" d="M4.5 0h7A1.5 1.5 0 0 1 13 1.5v13a1.5 1.5 0 0 1-1.5 1.5h-7A1.5 1.5 0 0 1 3 14.5v-13A1.5 1.5 0 0 1 4.5 0zM5 2v10h6V2zm3 11a1 1 0 1 0 0 2 1 1 0 0 0 0-2z"/></svg>
        +43 664 58 37 216
      </li>
    </ul>
  </div>

  <ul class="contact online">
    <li>
      <svg viewBox="0 0 16 16" aria-hidden="true"><path fill="currentColor" d="M1 3h14v10H1zm1.5 1.4v.4L8 8.6l5.5-3.8v-.4z"/></svg>
      lukas.fenwald@okr-gmbh.at
    </li>
    <li>
      <svg viewBox="0 0 16 16" aria-hidden="true"><circle cx="8" cy="8" r="6.6" fill="none" stroke="currentColor" stroke-width="1.6"/><path d="M1.5 8h13M8 1.4c-2.4 2.8-2.4 10.4 0 13.2M8 1.4c2.4 2.8 2.4 10.4 0 13.2" fill="none" stroke="currentColor" stroke-width="1.3"/></svg>
      www.okr-gmbh.at
    </li>
  </ul>
</section>

<section class="card card--back">
  <svg class="glow" viewBox="0 0 880 516" aria-hidden="true">
    <defs>
      <linearGradient id="glowFade" x1="0" y1="0" x2="0" y2="1">
        <stop offset="0" stop-color="#1e2249"/>
        <stop offset="0.45" stop-color="#6d6f8e"/>
        <stop offset="1" stop-color="#ffffff"/>
      </linearGradient>
      <clipPath id="glowCut"><rect x="0" y="150" width="880" height="366"/></clipPath>
    </defs>
    <ellipse cx="440" cy="264" rx="326" ry="208" fill="url(#glowFade)" clip-path="url(#glowCut)"/>
  </svg>
  <div class="back-brand">OKR</div>
  <div class="back-title">Dipl.-Ing.</div>
</section>

</body>
</html>
```